Weddings by Mirela
Wedding Planner
I NEED CONCEPTS WITH ENVELOPE, BUSINESS CARD AND PAPER...
NOT ONLY BUSINESS CARDS
THANK YOU
Hi everyone
thanks for sending.
please don't add Switzerland / schweiz...
i dont need to have the country on my business card. thanks a bunch. i am sorting out and get back to you now...
Designers: Logo .AI has been uploaded. Kindly refer to the creative brief. - Dean Pruitt
my logo should be there now....
thanks for drafts
plz upload the logo
My logo should be on business cards, letters and envelopes...
Writings should be same as used in my logo. Except if you add the address it should be kindof a "normal" writing.
i think it would look stupid if it will be same as in logo...
for questions, pls send message
cheers

```html
<!DOCTYPE html>
<html lang="en">
<head>
<meta charset="utf-8">
<title>Weddings by Mirela – Stationery</title>
<link rel="stylesheet" href="https://fonts.googleapis.com/css2?family=Cormorant+Garamond:wght@500&family=Lato:wght@400&display=swap">
<style>
  :root{
    --gold-dark:#a8752a;
    --gold:#c99a45;
    --gold-light:#ecd08e;
    --silver-dark:#8f8f8f;
    --silver:#c9c9c9;
    --silver-light:#f1f1f1;
    --paper:#ffffff;
    --ink:#555555;
    --bg:#ffffff;
    --edge:#dcdcdc;
  }
  *{box-sizing:border-box;margin:0;padding:0}
  html,body{width:1200px;height:785px;overflow:hidden;background:var(--bg)}
  .canvas{position:relative;width:1200px;height:785px}
  .sheet{position:absolute;background:var(--paper);border:1px solid var(--edge);overflow:hidden}
  .wave{position:absolute;left:0;bottom:0;width:100%}
  .brand{display:flex;align-items:center;gap:6px;font-family:"Cormorant Garamond",serif;font-weight:500;color:var(--gold);white-space:nowrap}
  .brand__dot{border-radius:50%;border:1.5px solid currentColor;flex:none}
  .small{font-family:"Lato",sans-serif;font-size:7px;line-height:1.5;color:var(--ink)}

  .letterhead{left:43px;top:84px;width:509px;height:648px}
  .letterhead .brand{position:absolute;left:26px;top:30px;font-size:30px}
  .letterhead .brand__dot{width:20px;height:20px}
  .letterhead__footer{position:absolute;left:24px;bottom:26px;color:#fff;font-size:7.5px}

  .card{position:absolute;width:216px;height:124px;box-shadow:0 1px 3px rgba(0,0,0,.15)}
  .card--front{left:571px;top:60px;width:233px;background:var(--paper);border:1px solid var(--edge);overflow:hidden}
  .card--front .brand{position:absolute;left:8px;top:10px;font-size:14px}
  .card--front .brand__dot{width:10px;height:10px}
  .card__name{position:absolute;left:124px;top:38px;font-family:"Cormorant Garamond",serif;font-size:10px;color:var(--gold);line-height:1.3}
  .card__name span{display:block;font-family:"Lato",sans-serif;font-size:6.5px;color:var(--ink)}
  .card__contact{position:absolute;left:8px;top:58px;font-size:5.5px}
  .card--back{left:828px;top:96px;background:var(--paper);border:1px solid var(--edge)}
  .card--silver{left:679px;top:228px;background:linear-gradient(160deg,var(--silver-light),var(--silver) 55%,var(--silver-dark))}
  .card--gold{left:919px;top:257px;background:linear-gradient(150deg,var(--gold-light),var(--gold) 45%,var(--gold-dark))}
  .card--centered{display:flex;align-items:center;justify-content:center}
  .card--centered .brand{font-size:20px}
  .card--centered .brand__dot{width:13px;height:13px}
  .card--gold .brand{color:#fff4dc}

  .envelope{left:571px;top:396px;width:564px;height:336px}
  .envelope__flap{position:absolute;left:0;top:0;width:100%;height:92px}
  .envelope__seal{position:absolute;left:258px;top:20px;width:48px;height:48px;border-radius:50%;background:linear-gradient(150deg,var(--silver-light),var(--silver-dark));border:3px solid var(--gold-dark)}
  .envelope .brand{position:absolute;left:16px;top:112px;font-size:30px}
  .envelope .brand__dot{width:20px;height:20px}
  .envelope__role{position:absolute;left:20px;top:170px;font-size:8px}
</style>
</head>
<body>
<div class="canvas">

  <section class="sheet letterhead" aria-label="Letterhead">
    <div class="brand"><span class="brand__dot"></span>Weddings by Mirela</div>
    <svg class="wave" width="509" height="120" viewBox="0 0 509 120" preserveAspectRatio="none" aria-hidden="true">
      <defs>
        <linearGradient id="lhGold" x1="0" x2="1"><stop offset="0" stop-color="#a8752a"/><stop offset=".5" stop-color="#ecd08e"/><stop offset="1" stop-color="#b8873a"/></linearGradient>
        <linearGradient id="lhSilver" x1="0" x2="1"><stop offset="0" stop-color="#f1f1f1"/><stop offset=".6" stop-color="#9a9a9a"/><stop offset="1" stop-color="#d6d6d6"/></linearGradient>
      </defs>
      <path d="M0 12 C160 0 300 40 509 30 L509 120 L0 120Z" fill="url(#lhGold)"/>
      <path d="M200 112 C330 90 430 88 509 70 L509 84 C430 100 330 104 200 118Z" fill="url(#lhSilver)"/>
    </svg>
    <p class="small letterhead__footer">Phone +41 79 812 34 56<br>info@weddingsbymirela.com, www.weddingsbymirela.com</p>
  </section>

  <section class="card card--front" aria-label="Business card front">
    <div class="brand"><span class="brand__dot"></span>Weddings by Mirela</div>
    <p class="card__name">Mirela Ostrov-Lind<span>Wedding Planner</span></p>
    <p class="small card__contact">Mirela Ostrov-Lind<br>Phone +41 79 812 34 56<br>info@weddingsbymirela.com<br>www.weddingsbymirela.com</p>
    <svg class="wave" width="233" height="26" viewBox="0 0 233 26" preserveAspectRatio="none" aria-hidden="true">
      <path d="M0 20 C80 15 160 8 233 4 L233 26 L0 26Z" fill="url(#lhGold)"/>
      <path d="M0 18 C80 13 160 6 233 2 L233 7 C160 11 80 18 0 23Z" fill="url(#lhSilver)"/>
    </svg>
  </section>

  <section class="card card--back card--centered" aria-label="Business card back">
    <div class="brand"><span class="brand__dot"></span>Weddings by Mirela</div>
  </section>

  <section class="card card--silver card--centered" aria-label="Business card, silver version">
    <div class="brand"><span class="brand__dot"></span>Weddings by Mirela</div>
  </section>

  <section class="card card--gold card--centered" aria-label="Business card, gold version">
    <div class="brand"><span class="brand__dot"></span>Weddings by Mirela</div>
  </section>

  <section class="sheet envelope" aria-label="Envelope">
    <svg class="envelope__flap" width="564" height="92" viewBox="0 0 564 92" preserveAspectRatio="none" aria-hidden="true">
      <path d="M0 0 L564 0 L564 60 C420 74 340 92 282 92 C224 92 144 74 0 60Z" fill="url(#lhGold)"/>
    </svg>
    <span class="envelope__seal" role="img" aria-label="Brand emblem seal"></span>
    <div class="brand"><span class="brand__dot"></span>Weddings by Mirela</div>
    <p class="small envelope__role">Wedding Planner</p>
    <svg class="wave" width="564" height="76" viewBox="0 0 564 76" preserveAspectRatio="none" aria-hidden="true">
      <path d="M0 14 C180 2 340 36 564 22 L564 76 L0 76Z" fill="url(#lhGold)"/>
      <path d="M220 70 C360 52 470 50 564 36 L564 46 C470 60 360 64 220 76Z" fill="url(#lhSilver)"/>
    </svg>
  </section>

</div>
</body>
</html>
```